VORELLI Industrial Maintenance

I offer repair and maintenance services of industrial mechanics in Quebec. I would like a creation that reflects confidence, competence, professionalism and dynamism. I like the orange color and the blue color.

Target Market(s)

Industries and Manufacturing companies using industrial machinery for the manufacture of their products.

Industry/Entity Type

Manufacturing

Contact Information for Business Card

VORELLI Maintenance Industrielle
Tél: (450)-318-5907
Courriel: vorelli.mnt@brastomail.com

Font styles to use
Sans Serif

Colors
f78f20
0455a3

Requirements
Must have
• My company name: VORELLI Maintenance Industrielle My phone: (450) -318-5907 My email: vorelli.mnt@brastomail.com
Nice to have
• Integrate a representative logo of the mechanics (gears, mechanical parts)

```html
<!DOCTYPE html>
<html lang="fr">
<head>
<meta charset="utf-8">
<title>VORELLI Maintenance Industrielle – Carte d'affaires</title>
<link rel="stylesheet" href="https://fonts.googleapis.com/css2?family=Poppins:wght@400;500;600;700&display=swap">
<style>
  :root {
    --brand-blue: #0455a3;
    --brand-orange: #f78f20;
    --orange-light: #fba652;
    --page-bg: #eceae6;
    --ink-light: #ffffff;
  }
  html, body {
    margin: 0;
    width: 1200px;
    height: 834px;
    overflow: hidden;
    background: var(--page-bg);
    font-family: "Poppins", sans-serif;
  }
  .business-card {
    position: absolute;
    left: 180px;
    top: 177px;
    width: 840px;
    height: 480px;
    overflow: hidden;
    box-shadow: 0 10px 30px rgba(0,0,0,0.18);
    color: var(--ink-light);
  }
  .card-shapes { position: absolute; inset: 0; }
  .brand-block {
    position: absolute;
    left: 0; right: 0;
    top: 62px;
    text-align: center;
  }
  .brand-dot {
    display: block;
    width: 34px; height: 34px;
    margin: 0 auto 10px;
    border-radius: 50%;
    background: var(--brand-orange);
  }
  .brand-name {
    margin: 0;
    font-size: 52px;
    font-weight: 700;
    letter-spacing: 2px;
    line-height: 1;
  }
  .brand-tagline {
    margin: 6px 0 0;
    font-size: 12px;
    font-weight: 500;
    letter-spacing: 1.5px;
    text-transform: uppercase;
  }
  .holder {
    position: absolute;
    left: 48px;
    top: 248px;
  }
  .holder-name {
    margin: 0;
    font-size: 26px;
    font-weight: 700;
    letter-spacing: 1px;
    text-transform: uppercase;
  }
  .holder-role {
    margin: 2px 0 0;
    font-size: 11px;
    font-weight: 500;
    letter-spacing: 0.5px;
    text-transform: uppercase;
  }
  .contact-list {
    position: absolute;
    left: 470px;
    top: 318px;
    margin: 0;
    padding: 0;
    list-style: none;
    font-size: 17px;
    font-weight: 500;
  }
  .contact-item {
    display: flex;
    align-items: center;
    gap: 12px;
    margin-bottom: 10px;
  }
  .contact-icon { width: 16px; height: 16px; flex: none; }
</style>
</head>
<body>
  <article class="business-card">
    <svg class="card-shapes" width="840" height="480" viewBox="0 0 840 480" aria-hidden="true">
      <defs>
        <radialGradient id="orangeGlow" cx="0.5" cy="0.75" r="0.6">
          <stop offset="0" stop-color="var(--orange-light)"/>
          <stop offset="1" stop-color="var(--brand-orange)"/>
        </radialGradient>
      </defs>
      <rect width="840" height="480" fill="url(#orangeGlow)"/>
      <polygon points="0,0 840,0 840,440 750,440 650,212 460,212 420,236 380,212 0,212" fill="var(--brand-blue)"/>
      <rect x="410" y="246" width="16" height="16" transform="rotate(45 418 254)" fill="var(--brand-orange)"/>
    </svg>

    <header class="brand-block">
      <span class="brand-dot"></span>
      <h1 class="brand-name">VORELLI</h1>
      <p class="brand-tagline">Maintenance Industrielle</p>
    </header>

    <section class="holder">
      <h2 class="holder-name">Julien Marchand</h2>
      <p class="holder-role">Électromécanicien</p>
    </section>

    <ul class="contact-list">
      <li class="contact-item">
        <svg class="contact-icon" viewBox="0 0 24 24"><path fill="#fff" d="M6.6 10.8a15.1 15.1 0 0 0 6.6 6.6l2.2-2.2a1 1 0 0 1 1-.25 11.4 11.4 0 0 0 3.6.57 1 1 0 0 1 1 1V20a1 1 0 0 1-1 1A17 17 0 0 1 3 4a1 1 0 0 1 1-1h3.5a1 1 0 0 1 1 1c0 1.25.2 2.45.57 3.57a1 1 0 0 1-.25 1z"/></svg>
        <span>(450)-318-5907</span>
      </li>
      <li class="contact-item">
        <svg class="contact-icon" viewBox="0 0 24 24"><path fill="#fff" d="M2 5h20v14H2z"/><path fill="none" stroke="var(--brand-orange)" stroke-width="2" d="M2 5l10 8 10-8"/></svg>
        <span>vorelli.mnt@brastomail.com</span>
      </li>
      <li class="contact-item">
        <svg class="contact-icon" viewBox="0 0 24 24"><path fill="#fff" d="M12 2a7 7 0 0 0-7 7c0 5.2 7 13 7 13s7-7.8 7-13a7 7 0 0 0-7-7zm0 9.5A2.5 2.5 0 1 1 12 6.5a2.5 2.5 0 0 1 0 5z"/></svg>
        <span>Quebec, Canada</span>
      </li>
    </ul>
  </article>
</body>
</html>
```